Everything fresh, everything new

When I take over the practice, I would like to breathe new life into the practice. I want a business card design that catches the eye and brings a breath of fresh air

```html
<!DOCTYPE html>
<html lang="de">
<head>
<meta charset="utf-8">
<title>Vitalwerk – Visitenkarte</title>
<link rel="stylesheet" href="https://fonts.googleapis.com/css2?family=Montserrat:wght@400;500;600;700&display=swap">
<style>
  :root {
    --page-bg-light: #dcdcdc;
    --page-bg-dark: #c6c6c6;
    --card-white: #ffffff;
    --card-dark: #545454;
    --brand-green: #9ccb4f;
    --swoosh-green: #bcd98a;
    --text-grey: #4a4a4a;
    --text-soft: #5a5a5a;
    --on-dark: #ffffff;
  }
  * { box-sizing: border-box; margin: 0; padding: 0; }
  html, body { width: 797px; height: 1200px; overflow: hidden; }
  body {
    background: radial-gradient(ellipse at 50% 45%, var(--page-bg-light), var(--page-bg-dark));
    font-family: "Montserrat", sans-serif;
    position: relative;
  }
  .card {
    position: absolute;
    left: 98px;
    width: 600px;
    height: 392px;
    overflow: hidden;
    box-shadow: 0 10px 28px rgba(0,0,0,0.18);
  }
  .card--front { top: 180px; background: var(--card-white); }
  .card--back { top: 628px; background: var(--card-dark); }

  .swoosh { position: absolute; inset: 0; width: 600px; height: 392px; }

  .holder { position: absolute; left: 39px; top: 58px; }
  .holder__name {
    color: var(--brand-green);
    font-weight: 700;
    font-size: 27px;
    line-height: 1;
    letter-spacing: -0.2px;
  }
  .holder__role {
    color: var(--text-soft);
    font-size: 16px;
    font-weight: 500;
    margin-top: 3px;
  }

  .wordmark {
    position: absolute;
    display: flex;
    align-items: center;
    gap: 8px;
    font-weight: 600;
    letter-spacing: -0.3px;
  }
  .wordmark__dot {
    width: 12px; height: 12px;
    border-radius: 50%;
    background: var(--brand-green);
  }
  .card--front .wordmark { right: 52px; top: 57px; font-size: 27px; color: var(--text-grey); }
  .card--back .wordmark {
    left: 50%; top: 50%;
    transform: translate(-50%, -50%);
    font-size: 34px; color: var(--on-dark);
  }

  .contact {
    position: absolute;
    left: 39px;
    top: 222px;
    list-style: none;
    color: var(--text-grey);
    font-size: 16px;
    line-height: 1.5;
  }
  .contact__item { display: flex; align-items: flex-start; gap: 10px; margin-bottom: 4px; }
  .contact__icon { width: 14px; height: 14px; margin-top: 5px; flex: none; fill: var(--brand-green); }

  .back-texture {
    position: absolute; inset: 0;
    background: radial-gradient(circle at 50% 50%, rgba(156,203,79,0.16), rgba(156,203,79,0.05) 55%, rgba(84,84,84,0) 80%);
  }
</style>
</head>
<body>

<section class="card card--front" aria-label="Visitenkarte Vorderseite">
  <svg class="swoosh" viewBox="0 0 600 392" aria-hidden="true">
    <g fill="none" stroke="var(--swoosh-green)">
      <circle cx="-80" cy="640" r="510" stroke-width="4"/>
      <circle cx="-80" cy="640" r="497" stroke-width="7"/>
      <circle cx="-80" cy="640" r="468" stroke-width="34"/>
    </g>
  </svg>

  <div class="holder">
    <p class="holder__name">Lena Hartwig</p>
    <p class="holder__role">President</p>
  </div>

  <div class="wordmark"><span class="wordmark__dot"></span><span>Vitalwerk</span></div>

  <ul class="contact">
    <li class="contact__item">
      <svg class="contact__icon" viewBox="0 0 14 14"><path d="M7 0a5 5 0 0 0-5 5c0 3.6 5 9 5 9s5-5.4 5-9a5 5 0 0 0-5-5zm0 7a2 2 0 1 1 0-4 2 2 0 0 1 0 4z"/></svg>
      <span>Neue Wege,<br>Lindenstraße 14</span>
    </li>
    <li class="contact__item">
      <svg class="contact__icon" viewBox="0 0 14 14"><path d="M3 1l2 3-1.3 1.3a8 8 0 0 0 5 5L10 9l3 2-1.5 2.5C6 13.5.5 8 .5 2.5z"/></svg>
      <span>555.203.4178</span>
    </li>
    <li class="contact__item">
      <svg class="contact__icon" viewBox="0 0 14 14"><path d="M0 3h14v1L7 8 0 4zM0 5.5l7 4 7-4V12H0z"/></svg>
      <span>info@vitalwerk.com</span>
    </li>
    <li class="contact__item">
      <svg class="contact__icon" viewBox="0 0 14 14"><circle cx="7" cy="7" r="6" fill="none" stroke="var(--brand-green)" stroke-width="1.4"/><path d="M1 7h12M7 1c-3 3-3 9 0 12M7 1c3 3 3 9 0 12" fill="none" stroke="var(--brand-green)" stroke-width="1.2"/></svg>
      <span>www.vitalwerk.com</span>
    </li>
  </ul>
</section>

<section class="card card--back" aria-label="Visitenkarte Rückseite">
  <div class="back-texture" role="img" aria-label="Dezente grüne Pinselkreise als Hintergrundmuster"></div>
  <div class="wordmark"><span class="wordmark__dot"></span><span>Vitalwerk</span></div>
</section>

</body>
</html>
```